Business Cards for a start up company

We are looking for a business card design for a start up company based in Ohio. The logo is attached. We are a healthcare company. We are open to all designs but want something professional but fun; creative, not boring

Industry/Entity Type

Healthcare

```html
<!DOCTYPE html>
<html lang="en">
<head>
<meta charset="utf-8">
<title>Bright Harbor Care — Business Cards</title>
<link rel="stylesheet" href="https://fonts.googleapis.com/css2?family=Montserrat:wght@500;600&display=swap">
<style>
  :root {
    --canvas: #f3f4f2;
    --card-white: #ffffff;
    --leaf-green: #8cc63f;
    --leaf-green-soft: #a3d25f;
    --navy: #1b2a5c;
    --sky-blue: #1ea7e1;
    --pale-blue: #8fd6f2;
    --text-white: #ffffff;
  }
  * { box-sizing: border-box; margin: 0; padding: 0; }
  html, body { width: 1200px; height: 873px; overflow: hidden; }
  body {
    background: var(--canvas);
    font-family: "Montserrat", Arial, sans-serif;
    position: relative;
  }
  .card {
    position: absolute;
    top: 282px;
    width: 540px;
    height: 309px;
    background: var(--card-white);
    box-shadow: 0 10px 28px rgba(0,0,0,0.16);
    overflow: hidden;
  }
  .card--services { left: 40px; }
  .card--contact { left: 620px; }
  .card__wave { position: absolute; inset: 0; width: 100%; height: 100%; }
  .brand {
    position: absolute;
    left: 22px;
    top: 22px;
    display: flex;
    align-items: center;
    gap: 8px;
  }
  .brand__dot {
    width: 14px; height: 14px; border-radius: 50%;
    background: var(--sky-blue);
  }
  .brand__name {
    font-weight: 600;
    font-size: 16px;
    color: var(--navy);
    letter-spacing: 0.2px;
    white-space: nowrap;
  }
  .service-list {
    position: absolute;
    left: 350px;
    top: 112px;
    list-style: none;
  }
  .service-list li {
    color: var(--text-white);
    font-weight: 500;
    font-size: 13px;
    line-height: 20px;
    letter-spacing: 0.4px;
    display: flex;
    align-items: center;
    gap: 7px;
  }
  .service-list li::before {
    content: "";
    width: 6px; height: 6px; border-radius: 50%;
    background: var(--pale-blue);
  }
  .holder {
    position: absolute;
    left: 340px;
    top: 84px;
    color: var(--navy);
    font-weight: 500;
    font-size: 12.5px;
    line-height: 17px;
    letter-spacing: 0.3px;
  }
  .contact-list {
    position: absolute;
    left: 320px;
    top: 166px;
    list-style: none;
    color: var(--navy);
    font-weight: 500;
    font-size: 12px;
    line-height: 19px;
  }
  .contact-list li { display: flex; align-items: center; gap: 7px; white-space: nowrap; }
  .contact-list__tag {
    width: 13px; height: 13px; border-radius: 50%;
    background: var(--sky-blue);
    color: var(--text-white);
    font-size: 8px;
    font-weight: 600;
    display: inline-flex; align-items: center; justify-content: center;
  }
</style>
</head>
<body>

  <section class="card card--services">
    <svg class="card__wave" viewBox="0 0 540 309" aria-hidden="true">
      <g transform="translate(110 0)">
        <path d="M182,0 L540,0 L540,309 L485,309 C390,300 255,282 205,195 C168,130 158,62 182,0 Z" fill="var(--leaf-green)"/>
        <path d="M176,0 C152,62 162,132 199,198 C250,288 385,306 482,309" fill="none" stroke="var(--navy)" stroke-width="3"/>
        <path d="M168,0 C144,64 154,136 191,202 C242,292 375,308 450,309" fill="none" stroke="var(--sky-blue)" stroke-width="2"/>
        <path d="M161,0 C137,66 147,140 184,206 C235,294 360,309 420,309" fill="none" stroke="var(--pale-blue)" stroke-width="1.5"/>
      </g>
      <circle cx="400" cy="95" r="62" fill="none" stroke="var(--leaf-green-soft)" stroke-width="14" opacity="0.7"/>
    </svg>
    <div class="brand">
      <span class="brand__dot"></span>
      <span class="brand__name">Bright Harbor Care</span>
    </div>
    <ul class="service-list">
      <li>DUMMY TEXT</li>
      <li>DUMMY TEXT</li>
      <li>DUMMY TEXT</li>
      <li>DUMMY TEXT</li>
      <li>DUMMY TEXT</li>
    </ul>
  </section>

  <section class="card card--contact">
    <svg class="card__wave" viewBox="0 0 540 309" aria-hidden="true">
      <g transform="translate(110 0)">
        <path d="M182,0 L540,0 L540,309 L485,309 C390,300 255,282 205,195 C168,130 158,62 182,0 Z" fill="var(--leaf-green)"/>
        <path d="M176,0 C152,62 162,132 199,198 C250,288 385,306 482,309" fill="none" stroke="var(--navy)" stroke-width="3"/>
        <path d="M168,0 C144,64 154,136 191,202 C242,292 375,308 450,309" fill="none" stroke="var(--sky-blue)" stroke-width="2"/>
        <path d="M161,0 C137,66 147,140 184,206 C235,294 360,309 420,309" fill="none" stroke="var(--pale-blue)" stroke-width="1.5"/>
      </g>
      <circle cx="385" cy="70" r="58" fill="none" stroke="var(--leaf-green-soft)" stroke-width="14" opacity="0.7"/>
    </svg>
    <div class="brand">
      <span class="brand__dot"></span>
      <span class="brand__name">Bright Harbor Care</span>
    </div>
    <p class="holder">BRIGHT HARBOR CARE<br>CEO/PRESIDENT</p>
    <ul class="contact-list">
      <li><span class="contact-list__tag">P</span>555-014-2277</li>
      <li><span class="contact-list__tag">E</span>hello@brightharborcare.com</li>
      <li><span class="contact-list__tag">A</span>#120, Bright Harbor Care</li>
    </ul>
  </section>

</body>
</html>
```